Business Card Design Project

I need a business card designed with these details on the front along with the logo attached on the front.

Address - 518/ 217 Wendlebury st Thornvale
Website - www.brackenhollowmasonry.com.au
Email - delwyn@brackenhollowmasonry.com.au
Fax - 1900 457 618
Mobile - 0471926038
Telephone - 1300517926
Licence number - 847263k

```html
<!DOCTYPE html>
<html lang="en">
<head>
<meta charset="utf-8">
<title>Bracken Hollow Masonry – Business Card</title>
<link href="https://fonts.googleapis.com/css2?family=Tinos:wght@700&family=Noto+Serif:ital,wght@1,400;1,700&display=swap" rel="stylesheet">
<style>
  :root{
    --rust:#8a4600;
    --rust-deep:#6e3300;
    --copper-light:#f2c2a8;
    --copper:#c47048;
    --stone-warm:#a4602e;
    --stone-dark:#7a3a16;
    --espresso:#311812;
    --paper:#ffffff;
    --ink:#3a1a12;
    --cream:#f3e6dc;
    --tile:#d9cbb4;
  }
  *{margin:0;padding:0;box-sizing:border-box}
  html,body{width:1200px;height:741px;overflow:hidden;background:#ffffff}
  .card{
    position:relative;width:1200px;height:741px;overflow:hidden;
    background:linear-gradient(90deg,var(--rust-deep) 0,var(--rust) 4%,var(--rust) 96%,var(--rust-deep) 100%);
  }
  .frame-line{position:absolute;background:linear-gradient(90deg,var(--copper),var(--copper-light),var(--copper))}
  .frame-line.top{left:0;top:0;width:1200px;height:8px}
  .frame-line.bottom{left:0;top:733px;width:1200px;height:8px}
  .frame-post{position:absolute;width:10px;background:linear-gradient(90deg,var(--copper),var(--copper-light),var(--copper))}
  .frame-post.left{left:40px;top:30px;height:700px}
  .frame-post.right{left:1136px;top:30px;height:700px}
  .stone-field{
    position:absolute;left:61px;top:44px;width:1072px;height:581px;
    background:
      radial-gradient(ellipse at 78% 40%,#c17a48 0,transparent 55%),
      radial-gradient(ellipse at 30% 90%,#9b5226 0,transparent 60%),
      linear-gradient(135deg,var(--stone-warm),var(--stone-dark));
  }
  .brand-panel{position:absolute;left:61px;width:521px;display:flex;align-items:center;padding-left:69px;gap:18px}
  .brand-panel.light{top:44px;height:205px;background:var(--paper)}
  .brand-panel.dark{top:249px;height:216px;background:var(--espresso)}
  .brand-mark{width:86px;height:86px;background:var(--tile);flex:none}
  .brand-name{font-family:"Tinos",serif;font-weight:700;font-size:29px;line-height:1.45;letter-spacing:.5px}
  .light .brand-name{color:var(--ink)}
  .dark .brand-name{color:var(--cream)}
  .accent-column{
    position:absolute;left:588px;top:50px;width:135px;height:415px;
    border:6px solid var(--copper);border-color:var(--copper-light) var(--copper) var(--copper) var(--copper-light);
    background:var(--rust);
  }
  .stone-feature{position:absolute;left:731px;top:44px;width:402px;height:421px;
    background:radial-gradient(ellipse at 55% 45%,#c48556 0,#a65f30 60%,#8e4a20 100%)}
  .contact{position:absolute;top:503px;font-family:"Noto Serif",serif;font-style:italic;font-size:19.5px;line-height:26px;color:var(--paper)}
  .contact.left{left:72px}
  .contact.right{left:798px}
  .contact b{font-weight:700}
  .rule{position:absolute;left:61px;top:625px;width:1072px;height:11px;background:var(--paper)}
  .base-band{position:absolute;left:61px;top:636px;width:1072px;height:50px;background:var(--rust)}
  .base-edge{position:absolute;left:61px;top:686px;width:1072px;height:7px;background:linear-gradient(90deg,var(--copper),var(--copper-light),var(--copper))}
</style>
</head>
<body>
<main class="card">
  <div class="frame-line top"></div>
  <div class="frame-post left"></div>
  <div class="frame-post right"></div>
  <div class="stone-field" role="img" aria-label="Warm sandstone texture"></div>
  <div class="stone-feature" role="img" aria-label="Large decorative monogram area on sandstone texture"></div>

  <section class="brand-panel light">
    <span class="brand-mark"></span>
    <h1 class="brand-name">BRACKEN HOLLOW<br>MASONRY</h1>
  </section>
  <section class="brand-panel dark">
    <span class="brand-mark"></span>
    <h2 class="brand-name">BRACKEN HOLLOW<br>MASONRY</h2>
  </section>

  <div class="accent-column"></div>

  <address class="contact left">
    Address - <b>518/ 217 Wendlebury st Thornvale</b><br>
    Website - <b>www.brackenhollowmasonry.com.au</b><br>
    Email - <b>delwyn@brackenhollowmasonry.com.au</b>
  </address>
  <address class="contact right">
    Fax - <b>1900 457 618</b><br>
    Mobile - <b>0471926038</b><br>
    Telephone - <b>1300517926</b><br>
    Licence number - <b>847263k</b>
  </address>

  <div class="rule"></div>
  <div class="base-band"></div>
  <div class="base-edge"></div>
  <div class="frame-line bottom"></div>
</main>
</body>
</html>
```